Counseling Practice Business Card

I need a professional looking business card incorporating my new logo that was just completed. Card needs to incorporate my name and title, description of my specialty, my address, my phone number, my fax number, my email and my website URL. I need to be able to choose design on/with different paper colors and textures.
I do not have a lot of business card ideas so I am open to anything but I want bold,sharp, clear card without additional designs other than my logo (see attached file info). I am open to different color backgrounds or paper colors including black. I do not like traditional brackets around area codes in phone number or dashes between numbers in phone number. Am open to other ways of presenting including periods between numbers as appropriate. I do not know enough to know what I like yet but I want card to coordinate and work together with my logo. My practice emphasizes natural mental health interventions so any use of color (with background paper color or the blue and green in my logo) that elicits nature is nice. In addition to black, any natural brown or wood looking background might be desirable also. Most of the offerings so far look very similar and boring.

Target Market(s)

Potential therapy clients and other professionals

Contact Information for Business Card

Card information:
Marcus T. Whitfield, Ph.D.
Licensed Clinical Psychologist
Integrative Health Coach
4812 Ferndale Pkwy NW
Suite 730
Duluth, GA 30096
(770) 555-0142 phone
(770) 555-0186 fax
drmarcuswhitfield@kelvora.com
pathbloomcounseling.com

Font styles to use
Serif
Sans Serif
Other font styles liked:
• anything that you think looks crisp, clear and easily readable

Requirements
Must have
• Any color used should coordinate with my logo design (see attached files).
• Card should be printed horizontally so top and bottom are longest sides of rectangle.
• Background color or paper color should complement and highlight logo. Do not like a white background. black, grey, brown or any color my logo would blend well with.
Nice to have
• I would like designer to utilize color to highlight letters/name or phone-fax-web symbols.
• Bottom edge of card could be highlighted if appropriate to an idea.
Should not have
• I would NOT want the card to have a pure white background at all.
• No clear cards.
• Cards should be oriented with long sides on bottom and top, NOT sides. DO NOT LIKE THIS THIN TALL ORIENTATION.

```html
<!DOCTYPE html>
<html lang="en">
<head>
<meta charset="utf-8">
<title>Pathbloom Counseling – Business Card</title>
<link rel="stylesheet" href="https://fonts.googleapis.com/css2?family=PT+Sans:wght@400;700&display=swap">
<style>
  :root {
    --backdrop: #3a3b3d;
    --paper: #b8856a;
    --ink: #3b2417;
    --ink-soft: #4a2e1f;
    --brand-blue: #2f86c8;
    --brand-green: #1f8a3e;
    --url-light: #dcc5b6;
    --divider: #8a5c45;
  }
  * { box-sizing: border-box; margin: 0; padding: 0; }
  html, body {
    width: 1200px; height: 960px; overflow: hidden;
    background: var(--backdrop);
    font-family: "PT Sans", "Myriad Pro", Arial, sans-serif;
  }
  .sheet {
    position: relative; width: 1200px; height: 960px;
    display: flex; flex-direction: column; align-items: center;
    justify-content: center; gap: 60px;
  }
  .card {
    position: relative; width: 700px; height: 400px;
    background: var(--paper); overflow: hidden;
    box-shadow: 0 8px 24px rgba(0,0,0,.35);
  }
  /* Back side */
  .card--back {
    display: flex; flex-direction: column; align-items: center; justify-content: center;
  }
  .brand-name--large {
    font-size: 52px; font-weight: 700; color: var(--brand-blue);
    letter-spacing: .5px;
  }
  .back-url {
    margin-top: 38px; font-size: 17px; letter-spacing: 4px; color: var(--url-light);
  }
  /* Front side */
  .card--front { display: flex; }
  .brand-block {
    width: 300px; display: flex; align-items: center; justify-content: center;
    padding-left: 20px; padding-bottom: 40px;
  }
  .brand-name--small {
    font-size: 30px; font-weight: 700; color: var(--ink); line-height: 1.1; text-align: left;
  }
  .divider {
    width: 1px; background: var(--divider); margin: 40px 0 70px;
  }
  .contact {
    padding: 42px 0 0 28px; color: var(--ink-soft); font-size: 17px; line-height: 22px;
  }
  .contact__name {
    font-weight: 700; font-size: 20px; letter-spacing: .4px; color: var(--ink);
    text-transform: uppercase;
  }
  .contact__address { margin-top: 8px; }
  .contact__lines { margin-top: 8px; list-style: none; }
  .contact__lines li { display: flex; align-items: center; gap: 8px; }
  .contact__lines svg { width: 14px; height: 14px; fill: var(--ink); flex: none; }
  .edge-trim {
    position: absolute; left: 0; right: 0; bottom: 0; height: 18px;
  }
  .edge-trim__green { position: absolute; left: 0; right: 0; top: 0; height: 3px; background: var(--brand-green); }
  .edge-trim__blue { position: absolute; left: 0; right: 0; bottom: 0; height: 12px; background: var(--brand-blue); }
</style>
</head>
<body>
<main class="sheet">
  <section class="card card--back" aria-label="Card back">
    <div class="brand-name brand-name--large">Pathbloom Counseling</div>
    <div class="back-url">pathbloomcounseling.com</div>
  </section>

  <section class="card card--front" aria-label="Card front">
    <div class="brand-block">
      <div class="brand-name brand-name--small">Pathbloom<br>Counseling</div>
    </div>
    <div class="divider"></div>
    <div class="contact">
      <div class="contact__name">Marcus T. Whitfield, Ph.D.</div>
      <div>Licensed Clinical Psychologist</div>
      <div>Integrative Health Coach</div>
      <div class="contact__address">
        4812 Ferndale Pkwy NW<br>Suite 730<br>Duluth, GA 30096
      </div>
      <ul class="contact__lines">
        <li>
          <svg viewBox="0 0 16 16" aria-hidden="true"><path d="M2 5c0-2 1-3 6-3s6 1 6 3v1h-3V5H5v1H2z M4 7h8l2 6H2z"/></svg>
          (770) 555-0142
        </li>
        <li>
          <svg viewBox="0 0 16 16" aria-hidden="true"><rect x="4" y="1" width="8" height="5"/><rect x="1" y="6" width="14" height="7" rx="1"/><rect x="4" y="11" width="8" height="4"/></svg>
          (770) 555-0186
        </li>
        <li>
          <svg viewBox="0 0 16 16" aria-hidden="true"><path d="M1 3h14v10H1z M1 3l7 6 7-6" stroke="#b8856a" stroke-width="1"/></svg>
          drmarcuswhitfield@kelvora.com
        </li>
        <li>
          <svg viewBox="0 0 16 16" aria-hidden="true"><circle cx="8" cy="8" r="7"/><path d="M1 8h14M8 1c-3 3-3 11 0 14M8 1c3 3 3 11 0 14" stroke="#b8856a" stroke-width="1" fill="none"/></svg>
          www.pathbloomcounseling.com
        </li>
      </ul>
    </div>
    <div class="edge-trim">
      <div class="edge-trim__green"></div>
      <div class="edge-trim__blue"></div>
    </div>
  </section>
</main>
</body>
</html>
```